Bold Creative Business Card for Digital Marketing Company (Contest)

NOTICE TO DESIGNERS: We understand this is how you make your living. Our commitment to you is to give you awesome and rapid feedback. If we don't think you are on the right track or have a chance of winning we will let you know right away so you don't have to focus your time with us and can continue to get work.

We respect the crowdsource community greatly. We have launched hundreds of crowdsource projects and will make this a great experience for you if you choose to participate (we hope you will!)

--------------
Brief
-------------

We are a cutting edge digital marketing company and we need a new, bold and creative business card designed to reflect who we are and what we do. We want our brand to stand out and be noticed.

The name of our company is: Tanglewood Web Marketing

Definition of Tanglewood:

a. a person pursuing rebellious, even potentially disruptive, policies or ideas:

b. a lone dissenter, as an intellectual, an artist, or a politician, who takes an independent stand apart from his or her associates

c. unorthodox, unconventional, nonconformist

Our businesses is helping small to medium size businesses with their online marketing using bold and creative outside the box strategies that get results.

We are an industry leader and need our business cards to stand out when we hand them out to people, and to be amazing so we stand out and "lead the pack"!

Our current website: http://www.tanglewoodwebmarketing.example

We are rebranding our site to reflect the new logo we just got but you will at least have an idea of who we are and what we do.

Colors We Want: We would like to see burnt Orange, Dark Blue, Gray and/or Black.

We need a front and back designed!

Be creative! Even to the point of creative-shaped business cards. Think outside the box. Let nothing stop your imagination! At the very least, we know that we want business cards that are not the US Standard 2"x3.5"... but rather the wider 3.35"x2.17" (European Standard) with rounded corners if you want to stick with a rectangular shape.

On the front we need:

Our Logo
Place for a name ie Paul Dravecki
Place for our phone number (612) 555 - 8806
Place for email name@tanglewoodwebmarketing.example
Place for our website www.TanglewoodWebMarketing.example

Optional... Place for a headshot photo of the person who the business card will be used for

On the back we need:

The wording... FREE VIDEO SERIES! "10 Bold Moves To Grow Your Company Now!" www.TanglewoodWebMarketing.example/BoldMoves

We are excited to see what you come up with.

Thank you for your interests and for participating in this contest!
Updates

Hi everyone! Thanks for all your submissions. However, we feel that most of you are "missing" what we're looking for. Almost all of the designs that have come in are what we would call "standard", "generic", or "typical". We are looking for something creative, different, attention-getting, a business card that would stand out amongst a stack of other business cards. I've shot this video: http://clipviewer.example/t/qWpZtRbHmsd Please take the time to review it. Let us know if you have questions. Thanks!

Target Market(s)

Our target market is small to medium sized business owners who need help with their online marketing.

Industry/Entity Type

Marketing

Font styles to use
Sans Serif

Colors
0355a3
85acd3
f78f20
f37022
faa54b
f68d4d

Requirements
Must have
• On the front we need:

Our Logo

Be CREATIVE! INTERESTING!

On the back we need:

Use the colors from our logo!
Nice to have
• Optional... Place for a headshot photo of the person who the business card will be used for.
Should not have
• Boring, "traditional" look and feel. We want and need to stand out!

```html
<!DOCTYPE html>
<html lang="en">
<head>
<meta charset="utf-8">
<title>Tanglewood Web Marketing – Business Card</title>
<link rel="stylesheet" href="https://fonts.googleapis.com/css2?family=Lato:ital,wght@0,300;0,400;0,700;1,700&display=swap">
<style>
  :root {
    --blue-dark: #0a3f86;
    --blue: #0355a3;
    --blue-light: #3a9bd0;
    --blue-pale: #85acd3;
    --orange: #f37022;
    --orange-soft: #faa54b;
    --ink: #1d1d1f;
    --grey: #6b6e72;
    --paper: #ffffff;
    --page: #ececec;
  }
  * { box-sizing: border-box; margin: 0; padding: 0; }
  html, body { width: 1200px; height: 1023px; overflow: hidden; }
  body {
    background: var(--page);
    font-family: "Lato", Arial, sans-serif;
    position: relative;
  }
  .card {
    position: absolute;
    left: 280px;
    width: 640px;
    height: 414px;
    border-radius: 28px;
    overflow: hidden;
    box-shadow: 0 6px 18px rgba(0,0,0,.18);
  }
  /* Front */
  .card-front { top: 62px; background: var(--paper); }
  .front-swoosh { position: absolute; left: 0; top: 0; width: 640px; height: 414px; }
  .headshot {
    position: absolute; top: 30px; right: 40px;
    width: 96px; height: 80px;
    border: 3px solid #d7d9dc;
    background: linear-gradient(160deg, #a8b9c9 0%, #c79e80 55%, #5c6f82 100%);
  }
  .holder { position: absolute; top: 124px; right: 40px; text-align: right; }
  .holder-name { font-size: 30px; font-weight: 400; color: var(--ink); letter-spacing: .3px; }
  .holder-role { font-size: 19px; color: var(--ink); margin-top: 2px; }
  .brand-front {
    position: absolute; left: 44px; top: 168px;
    display: flex; align-items: center; gap: 12px;
  }
  .brand-square { width: 28px; height: 28px; background: var(--orange); }
  .brand-name-front { font-size: 24px; font-weight: 700; color: var(--orange); letter-spacing: .4px; }
  .contact {
    position: absolute; right: 40px; top: 222px;
    list-style: none; text-align: right;
  }
  .contact li {
    display: flex; justify-content: flex-end; align-items: center; gap: 12px;
    font-size: 19px; color: var(--ink); line-height: 30px;
  }
  .contact-icon {
    width: 16px; height: 16px; border-radius: 3px;
    background: var(--orange-soft);
    display: flex; align-items: center; justify-content: center;
  }
  .contact-icon svg { width: 12px; height: 12px; }
  /* Back */
  .card-back {
    top: 548px;
    background: linear-gradient(135deg, #1f6ec2 0%, var(--blue) 45%, var(--blue-dark) 100%);
    color: #fff;
  }
  .brand-back {
    position: absolute; left: 0; right: 0; top: 112px;
    display: flex; justify-content: center; align-items: center; gap: 16px;
  }
  .brand-back .brand-square { width: 40px; height: 40px; }
  .brand-name-back { font-size: 36px; font-weight: 700; color: #fff; letter-spacing: .5px; }
  .offer {
    position: absolute; left: 0; right: 0; top: 212px; text-align: center;
  }
  .offer-title { font-size: 27px; font-weight: 700; font-style: italic; color: var(--orange-soft); }
  .offer-url { font-size: 21px; font-weight: 700; color: #fff; margin-top: 12px; }
</style>
</head>
<body>

<section class="card card-front" aria-label="Business card front">
  <svg class="front-swoosh" viewBox="0 0 640 414" aria-hidden="true">
    <defs>
      <linearGradient id="swooshBlue" x1="0" y1="0" x2="1" y2="0">
        <stop offset="0" stop-color="#0b56a8"/>
        <stop offset="1" stop-color="#3aa3d6"/>
      </linearGradient>
    </defs>
    <path d="M0,322 C160,384 330,396 640,374 L640,414 L0,414 Z" fill="url(#swooshBlue)"/>
    <path d="M0,306 C160,372 330,388 560,384" fill="none" stroke="#f78f20" stroke-width="3"/>
    <path d="M330,414 C372,394 470,378 640,368" fill="none" stroke="#ffffff" stroke-width="6"/>
  </svg>

  <div class="headshot" role="img" aria-label="Headshot photo of the card holder"></div>

  <div class="holder">
    <p class="holder-name">Paul Dravecki</p>
    <p class="holder-role">Director</p>
  </div>

  <div class="brand-front">
    <span class="brand-square"></span>
    <span class="brand-name-front">Tanglewood Web Marketing</span>
  </div>

  <ul class="contact">
    <li>(612) 555 - 8806
      <span class="contact-icon"><svg viewBox="0 0 12 12"><path d="M3,1 L5,3.5 L4,5 C4.6,6.4 5.6,7.4 7,8 L8.5,7 L11,9 L10,11 C5.5,10.6 1.4,6.5 1,2 Z" fill="#fff"/></svg></span>
    </li>
    <li>@tanglewoodwebmarketing.example
      <span class="contact-icon"><svg viewBox="0 0 12 12"><rect x="1.5" y="3" width="9" height="6" fill="none" stroke="#fff" stroke-width="1.2"/><path d="M1.5,3 L6,6.5 L10.5,3" fill="none" stroke="#fff" stroke-width="1.2"/></svg></span>
    </li>
    <li>www.TanglewoodWebMarketing.example
      <span class="contact-icon"><svg viewBox="0 0 12 12"><circle cx="6" cy="6" r="4.5" fill="none" stroke="#fff" stroke-width="1.1"/><ellipse cx="6" cy="6" rx="2" ry="4.5" fill="none" stroke="#fff" stroke-width="1"/><path d="M1.5,6 H10.5" stroke="#fff" stroke-width="1"/></svg></span>
    </li>
  </ul>
</section>

<section class="card card-back" aria-label="Business card back">
  <div class="brand-back">
    <span class="brand-square"></span>
    <span class="brand-name-back">Tanglewood Web Marketing</span>
  </div>
  <div class="offer">
    <p class="offer-title">“10 Bold Moves To Grow Your Company Now!”</p>
    <p class="offer-url">www.TanglewoodWebMarketing.example/BoldMoves</p>
  </div>
</section>

</body>
</html>
```